Business Card Design Project

We have a logo, but would like to expand the use of it into a business card design. We are a B2B technology exchange platform for institutional investors to invest excess cash into short term assets matching their credit and pricing parameters. The assets are fractionalized and investors invest in portions.

Our customers are large, institutional, financial companies who are a bit traditional. We are high energy rebels with a cause...we are a disruptive technology and want to be viewed as a game changer but we need to present an image of trustworthiness and secure.

We are open not only to the image design but the material, die cut, etc. but want to stay in the traditional size of a business card.

We have other formats of the logo if needed. Our website is www.brambleharbor.com

I have posted a powerpoint template that we have been using.  This should not be considered the template we will use (after business cards we will have another project to incorporate business card design into powerpoint template) but just to give you a flavor of where we have been and have used in the past.

Target Market(s)

Institutional investors, asset managers, large fund institutions

Industry/Entity Type

Financial

Requirements
Must have
• Our logo
Traditional size
Nice to have
• unique use of logo, unique material, die cut, etc
Crisp, clean look
Use of both sides of card in a creative manner

```html
<!DOCTYPE html>
<html lang="en">
<head>
<meta charset="utf-8">
<title>Bramble Harbor – Business Card</title>
<link rel="stylesheet" href="https://fonts.googleapis.com/css2?family=Ubuntu:wght@400;500&display=swap">
<style>
  :root {
    --backdrop: #a59e98;
    --card: #ffffff;
    --card-shade: #e6e7e8;
    --ink: #58595b;
    --ink-strong: #4d4e50;
    --accent: #f7941d;
    --pattern: #77787b;
  }
  * { margin: 0; padding: 0; box-sizing: border-box; }
  html, body {
    width: 1200px; height: 800px; overflow: hidden;
    background: var(--backdrop);
    font-family: "Ubuntu", sans-serif;
    color: var(--ink);
  }
  .card {
    position: absolute;
    width: 660px; height: 343px;
    border: 2px solid var(--card);
    background: linear-gradient(90deg, var(--card-shade) 0%, var(--card) 40%, var(--card) 100%);
    overflow: hidden;
  }
  .card--front { left: 290px; top: 34px; }
  .card--back  { left: 289px; top: 424px; }

  .pattern { position: absolute; left: 0; top: 0; }

  .wordmark {
    position: absolute;
    font-weight: 500;
    color: var(--ink);
    white-space: nowrap;
    display: flex; align-items: center;
  }
  .wordmark__dot { border-radius: 50%; background: var(--accent); display: inline-block; }
  .wordmark--small { left: 19px; top: 24px; font-size: 21px; line-height: 1.05; }
  .wordmark--small .wordmark__dot { width: 14px; height: 14px; margin-left: 8px; }
  .wordmark--large {
    left: 0; right: 0; top: 120px; justify-content: center;
    font-size: 58px; letter-spacing: 1px; color: var(--ink);
  }
  .wordmark--large .wordmark__dot { width: 38px; height: 38px; margin-left: 16px; }

  .person { position: absolute; right: 251px; top: 126px; text-align: right; }
  .person__name { font-size: 33px; font-weight: 400; color: var(--ink-strong); line-height: 1.1; }
  .person__title { font-size: 22px; color: var(--accent); margin-right: 31px; line-height: 1.2; }

  .address {
    position: absolute; left: 284px; top: 212px;
    font-size: 16px; line-height: 19.5px; color: var(--ink-strong);
  }
  .contact {
    position: absolute; left: 37px; top: 283px;
    list-style: none; font-size: 16px; line-height: 22px; color: var(--ink-strong);
  }
  .contact__label { color: var(--accent); display: inline-block; width: 21px; }

  .card__footer {
    position: absolute; left: 23px; right: 26px; bottom: 8px;
    display: flex; justify-content: space-between;
    font-size: 19px; color: var(--ink);
  }
  .card__footer .label { color: var(--accent); font-size: 17px; margin-right: 4px; }
</style>
</head>
<body>

<section class="card card--front">
  <svg class="pattern" width="656" height="339" viewBox="0 0 656 339" role="img" aria-label="Grey and white geometric triangle pattern">
    <polygon fill="var(--pattern)" points="373,0 656,0 656,339 515,339 444,268 515,268 515,203 373,203 444,133 373,66"/>
  </svg>

  <div class="wordmark wordmark--small">Bramble<br>Harbor<span class="wordmark__dot"></span></div>

  <div class="person">
    <h1 class="person__name">Daniel Whitcombe</h1>
    <p class="person__title">President &amp; CEO</p>
  </div>

  <address class="address" style="font-style:normal">
    2190 Harbor Crest Drive<br>
    Suite 410<br>
    Alder Point, CA 93010
  </address>

  <ul class="contact">
    <li><span class="contact__label">P</span>805.555.0142 c 818.555.0187</li>
    <li><span class="contact__label">E</span>dwhitcombe@brambleharbor.com</li>
  </ul>
</section>

<section class="card card--back">
  <div class="wordmark wordmark--large">BRAMBLE HARBOR<span class="wordmark__dot"></span></div>
  <div class="card__footer">
    <span><span class="label">profile</span>danielwhitcombe</span>
    <span>www.brambleharbor.com</span>
  </div>
</section>

</body>
</html>
```